Bold Website Redesign for a Disruptive Training Brand

Brightmoor Labs is a bold, no-fluff sales & leadership training company powered by AI-driven practice and behavioral science. We’ve already built our website structure and copy in Craftly.io — now we need a designer to fully transform the visual design across all pages (Home, Approach, Programs, About, Contact).
We’re looking for a modern, memorable, high-performance aesthetic that blends human energy, science, and tech without feeling corporate or safe. Clean, bold typography, fluid layout, strong emotional hero moments, subtle motion, and imagery that mixes real people with abstract scientific/tech visuals.Because our clients are primarily North American, please ensure any human photography or AI-generated imagery reflects a North American business context and demographics (modern, diverse, and realistic).

Your job is visual redesign only — no coding required.
The final design must be practical to rebuild inside Craftly.io.

A full, detailed creative brief (plus logo files) is included in the uploaded files.
If you can bring a mix of edge, intelligence, and strong visual storytelling, we’d love to see your work.

Website is already built in Craftly.io at - https://brightmoor-website-tempdesign.craftly.app — structure is set, visuals need redesign.

```html
<!DOCTYPE html>
<html lang="en">
<head>
<meta charset="utf-8">
<title>Brightmoor Labs — About &amp; Contact</title>
<link href="https://fonts.googleapis.com/css2?family=Inter:wght@300;400;500;600;700&display=swap" rel="stylesheet">
<style>
:root{
  --board:#dcdcdc;
  --page:#ffffff;
  --nav:#f7f8fa;
  --ink:#0f2a4a;
  --text:#1e2f45;
  --muted:#4a5a70;
  --brand:#1f56c8;
  --grad-a:#0a56f0;
  --grad-b:#13c3f2;
  --footer:#04203f;
  --footer-text:#c9d6e6;
  --line:#2a4566;
  --hero-a:#123057;
  --hero-b:#1f5e9c;
  --hero-c:#2f9bd0;
  --field:#8a98ab;
}
*{box-sizing:border-box;margin:0;padding:0}
html,body{width:1200px;height:849px;overflow:hidden;background:var(--board);font-family:"Inter",Arial,sans-serif;color:var(--text)}
.board{position:relative;width:1200px;height:849px}
.page{position:absolute;top:122.3px;width:740px;height:1157px;background:var(--page);transform:scale(0.5226);transform-origin:0 0;overflow:hidden;outline:1px solid #c4c8ce}
.page--about{left:194.4px}
.page--contact{left:618.8px}
.abs{position:absolute}
.center{text-align:center;left:0;right:0}

/* nav */
.nav{position:absolute;left:0;top:0;width:740px;height:28px;background:var(--nav);border-bottom:1px solid #e3e6ea}
.nav__brand{position:absolute;left:112px;top:9px;display:flex;align-items:center;gap:5px;font-size:9px;letter-spacing:.6px;color:var(--ink);font-weight:500}
.nav__dot{width:12px;height:9px;background:var(--brand);border-radius:1px}
.nav__links{position:absolute;left:430px;top:11px;display:flex;gap:11px;font-size:5px;color:#6a7787}
.nav__links .is-active{color:var(--brand);border-bottom:1px solid var(--brand);padding-bottom:1px}
.nav__cta{position:absolute;left:593px;top:7px;width:37px;height:15px;border-radius:3px;background:linear-gradient(90deg,var(--grad-a),var(--grad-b));color:#fff;font-size:4.5px;display:flex;align-items:center;justify-content:center}

/* hero */
.hero{position:absolute;left:0;top:28px;width:740px;height:417px;clip-path:polygon(0 0,100% 0,100% 72%,0 100%)}
.hero--about{background:linear-gradient(160deg,var(--hero-a) 0%,var(--hero-b) 55%,var(--hero-c) 100%)}
.hero--contact{background:linear-gradient(120deg,var(--hero-a) 0%,var(--hero-b) 40%,var(--hero-c) 100%)}
.hero__title{top:124px;font-size:17px;font-weight:300;color:#fff}
.hero__sub{top:153px;font-size:8.5px;color:#e6f0fb}
.hero__body{top:168px;font-size:6px;line-height:8px;color:#d9e7f6}

.wordmark{top:430px;font-size:22px;font-weight:600;color:var(--brand);letter-spacing:.5px}
.h2{font-size:17px;font-weight:300;color:var(--ink)}
.lead-bold{font-size:8.5px;font-weight:600;color:var(--ink)}
.lead{font-size:8.5px;color:var(--ink)}
.small{font-size:6px;line-height:8.3px;color:var(--text)}
.small b{font-weight:700;color:var(--ink)}

/* columns */
.col{position:absolute;text-align:center}
.col--belief{left:82px;width:270px;top:566px}
.col--story{left:405px;width:275px;top:566px}
.col p{margin-top:6px}

/* team */
.team{position:absolute;left:143px;width:455px;top:746px;display:flex;justify-content:space-between}
.member{width:150px;text-align:center;display:flex;flex-direction:column;align-items:center}
.member__photo{width:64px;height:64px;border-radius:50%;background:radial-gradient(circle at 50% 40%,#b99a82 0%,#6d5a4d 55%,#3a3a44 100%)}
.member__name{font-size:13px;font-weight:300;color:var(--ink);margin-top:6px;line-height:15px}
.member__role{font-size:6.5px;color:var(--text);margin-top:2px}
.member__bio{font-size:6.3px;line-height:8.3px;color:var(--text);margin-top:8px;width:140px}

/* footer */
.footer{position:absolute;left:0;top:987px;width:740px;height:170px;background:var(--footer);color:var(--footer-text)}
.footer__brand{position:absolute;left:109px;top:33px;display:flex;align-items:center;gap:5px;font-size:8px;color:#fff}
.footer__brand i{width:11px;height:8px;background:#fff;border-radius:1px}
.footer__tag{position:absolute;left:109px;top:52px;width:120px;font-size:4.8px;line-height:7px}
.footer__col{position:absolute;top:30px;font-size:4.8px;line-height:11px}
.footer__col h4{font-size:7px;font-weight:600;color:#fff;margin-bottom:2px}
.footer__col--links{left:244px}
.footer__col--touch{left:379px}
.ico{display:inline-block;width:6px;height:5px;vertical-align:-1px;margin-right:3px}
.socials{display:flex;gap:3px;margin-top:1px}
.socials span{width:7px;height:7px;border:0.7px solid var(--footer-text);border-radius:50%}
.footer__rule{position:absolute;left:109px;top:123px;width:521px;height:1px;background:var(--line)}
.footer__copy{position:absolute;left:109px;top:137px;font-size:4.8px}
.footer__legal{position:absolute;left:586px;top:137px;font-size:4.8px;display:flex;gap:10px}

/* contact form */
.form{position:absolute;left:133px;top:548px;width:221px}
.form__title{font-size:17px;font-weight:300;color:var(--ink)}
.form__desc{font-size:6px;line-height:8px;margin-top:2px}
.field{margin-top:7px}
.field label{display:block;font-size:6px;color:var(--ink);margin-bottom:3px}
.field__box{height:17px;border:1px solid var(--field);border-radius:3px}
.field__box--area{height:70px}
.form__send{margin-top:14px;height:16px;border-radius:3px;background:linear-gradient(90deg,var(--grad-a),var(--grad-b));color:#fff;font-size:5px;display:flex;align-items:center;justify-content:center}

.info{position:absolute;left:396px;top:548px;width:215px}
.info__item{display:flex;gap:6px;margin-top:11px}
.info__item + .info__item{margin-top:25px}
.info__icon{width:18px;height:18px;border-radius:50%;background:var(--grad-a);flex:none;display:flex;align-items:center;justify-content:center}
.info__label{font-size:6px;font-weight:600;color:var(--ink)}
.info__val{font-size:6px;line-height:8px;color:var(--ink)}
.info__quote{margin-top:16px;font-size:6px;line-height:8px;text-align:center;color:var(--text)}
</style>
</head>
<body>
<div class="board">

  <section class="page page--about">
    <header class="nav">
      <div class="nav__brand"><span class="nav__dot"></span>BRIGHTMOOR LABS</div>
      <nav class="nav__links"><span>Home</span><span>Approach</span><span>Programs</span><span class="is-active">About</span><span>Contact</span></nav>
      <div class="nav__cta">Let's Talk</div>
    </header>
    <div class="hero hero--about" role="img" aria-label="Photo of a training room full of seated professionals facing a presenter, tinted blue"></div>
    <h1 class="abs center hero__title">The problem with most training?</h1>
    <p class="abs center hero__sub">It stops. Right when it should start working.</p>
    <p class="abs center hero__body">We built Brightmoor Labs to change that. Our platform keeps your people practicing, refining,<br>and improving — long after the workshop ends. It's the follow-through training never had.</p>

    <div class="abs center wordmark">Brightmoor Labs</div>
    <h2 class="abs center h2" style="top:488px">What is Brightmoor Labs</h2>
    <p class="abs center lead-bold" style="top:511px">Being on the same wavelength means more than agreement — it's about alignment and momentum.</p>
    <p class="abs center small" style="top:530px">We built Brightmoor Labs to change that. Our platform keeps your people practicing, refining, and improving — long after the workshop ends.<br>It's the follow-through training never had.</p>

    <div class="col col--belief">
      <h3 class="h2">Our Belief</h3>
      <p class="small"><b>Lasting growth isn't about charisma in the classroom.<br>It's about practice, feedback, and proof.</b></p>
      <p class="small">We make skill building continuous — so leaders and teams don't just learn once;<br>they keep getting better. The science is clear: behavior change requires<br>consistent practice over time. Yet most training programs deliver a one-time<br>event and hope for the best.</p>
      <p class="small">Brightmoor Labs closes that gap by turning sustainment into design<br>— making it automatic, measurable, and real.</p>
    </div>
    <div class="col col--story">
      <h3 class="h2">Our Story</h3>
      <p class="small"><b>We've been on both sides of the learning equation — as executives and<br>consultants. Again and again, we saw training stop where growth should start.</b></p>
      <p class="small">Teams would leave workshops energized and equipped with new frameworks.<br>But within weeks, the momentum faded. Leaders didn't have time to reinforce.<br>Learners didn't have structured practice. And organizations couldn't measure<br>what actually stuck.</p>
      <p class="small">Brightmoor Labs was born from that frustration — and the conviction that there's<br>a better way. We've designed a system that makes sustainment automatic,<br>combining behavioral science with AI to create learning that lasts.</p>
    </div>

    <h2 class="abs center h2" style="top:712px">Leadership Team</h2>
    <div class="team">
      <div class="member">
        <div class="member__photo" role="img" aria-label="Portrait photo of Owen Hale"></div>
        <div class="member__name">Owen Hale</div>
        <div class="member__role">Co-Founder &amp; CEO</div>
        <p class="member__bio">Growth strategist and technologist, expert in scaling teams through insight and analytics. Owen brings deep experience in translating data into actionable capability development.</p>
      </div>
      <div class="member">
        <div class="member__photo" role="img" aria-label="Portrait photo of Marcus Dunleavy"></div>
        <div class="member__name">Marcus Dunleavy</div>
        <div class="member__role">Co-Founder &amp; Chief Strategy Officer</div>
        <p class="member__bio">Veteran leader in organizational alignment and culture transformation. Marcus has helped hundreds of companies build cohesive, high-performing teams at scale.</p>
      </div>
      <div class="member">
        <div class="member__photo" role="img" aria-label="Portrait photo of Grant Ellison"></div>
        <div class="member__name">Grant Ellison</div>
        <div class="member__role">Co-Founder &amp; Chief Growth Officer</div>
        <p class="member__bio">Expert in human capital and science-based training design, focused on measurable performance outcomes. Grant ensures our programs deliver real, lasting results.</p>
      </div>
    </div>

    <h2 class="abs center h2" style="top:911px">What Drives Us</h2>
    <p class="abs center small" style="top:941px">We believe leadership and sales excellence are skills that can be practiced, measured, and sustained. Our work makes that practice<br>automatic — so growth depends on design, not intention.</p>

    <footer class="footer">
      <div class="footer__brand"><i></i>Brightmoor Labs</div>
      <p class="footer__tag">Making learning that sticks through AI-driven sustainment and behavioral science.</p>
      <div class="footer__col footer__col--links"><h4>Quick Links</h4>Home<br>Approach<br>Programs<br>About<br>Contact</div>
      <div class="footer__col footer__col--touch"><h4>Get in Touch</h4>
        <svg class="ico" viewBox="0 0 12 10"><rect x="0.5" y="0.5" width="11" height="9" fill="none" stroke="currentColor"/><path d="M1 1l5 4 5-4" fill="none" stroke="currentColor"/></svg>contact@brightmoorlabs.com<br>
        <svg class="ico" viewBox="0 0 12 10"><path d="M2 1l2 0 1 2-1 1q1 2 3 3l1-1 2 1v2q-6 0-8-8z" fill="none" stroke="currentColor"/></svg>+1 (555) 014-2290<br>
        <svg class="ico" viewBox="0 0 12 10"><path d="M6 9.5C3 6 2.5 5 2.5 4a3.5 3.5 0 017 0c0 1-.5 2-3.5 5.5z" fill="none" stroke="currentColor"/></svg>2750 Harlow Ave Suite 210<br><span style="margin-left:9px">Denver, CO 80205</span>
        <div class="socials"><span></span><span></span></div>
      </div>
      <div class="footer__rule"></div>
      <div class="footer__copy">© 2025 Brightmoor Labs. All rights reserved.</div>
      <div class="footer__legal"><span>Terms</span><span>Privacy</span></div>
    </footer>
  </section>

  <section class="page page--contact">
    <header class="nav">
      <div class="nav__brand"><span class="nav__dot"></span>BRIGHTMOOR LABS</div>
      <nav class="nav__links"><span>Home</span><span>Approach</span><span>Programs</span><span>About</span><span class="is-active">Contact</span></nav>
      <div class="nav__cta">Let's Talk</div>
    </header>
    <div class="hero hero--contact" role="img" aria-label="Photo of colleagues working together at computer desks in an office, tinted blue"></div>

    <div class="abs center wordmark">Brightmoor Labs</div>
    <h2 class="abs center h2" style="top:488px">Make it Happen</h2>
    <p class="abs center lead" style="top:511px">Lasting growth starts with one — a real conversation about what's working, what's not, and what's possible.</p>

    <div class="form">
      <h3 class="form__title">Get in Touch</h3>
      <p class="form__desc">Whether you're exploring training or curious about our model,<br>we'll help you find the right path — no pressure, no script.</p>
      <div class="field"><label>Name *</label><div class="field__box"></div></div>
      <div class="field"><label>Organization *</label><div class="field__box"></div></div>
      <div class="field"><label>Email *</label><div class="field__box"></div></div>
      <div class="field"><label>Message *</label><div class="field__box field__box--area"></div></div>
      <div class="form__send">Send Message</div>
    </div>

    <div class="info">
      <h3 class="form__title">Contact Information</h3>
      <p class="form__desc">Reach out through any of these channels, and we'll respond<br>quickly to start the conversation.</p>
      <div class="info__item">
        <span class="info__icon"><svg width="9" height="7" viewBox="0 0 12 10"><rect x="0.5" y="0.5" width="11" height="9" fill="none" stroke="#fff"/><path d="M1 1l5 4 5-4" fill="none" stroke="#fff"/></svg></span>
        <div><div class="info__label">Email</div><div class="info__val">contact@brightmoorlabs.pro</div></div>
      </div>
      <div class="info__item">
        <span class="info__icon"><svg width="9" height="9" viewBox="0 0 12 12"><path d="M2 1h2.5l1 3-1.5 1q1 2.5 3 3.5l1-1.5 3 1V11q-8 0-9-10z" fill="none" stroke="#fff"/></svg></span>
        <div><div class="info__label">Phone</div><div class="info__val">+1 (555) 014-2290</div></div>
      </div>
      <div class="info__item">
        <span class="info__icon"><svg width="8" height="9" viewBox="0 0 12 12"><path d="M6 11.5C2.5 7.5 2 6 2 4.5a4 4 0 018 0c0 1.5-.5 3-4 7z" fill="none" stroke="#fff"/><circle cx="6" cy="4.5" r="1.4" fill="none" stroke="#fff"/></svg></span>
        <div><div class="info__label">Address</div><div class="info__val">2750 Harlow Ave Suite 210<br>Denver, CO 80205</div></div>
      </div>
      <p class="info__quote">"We're here to help you explore what's possible. No hard sell,<br>just honest conversation about making learning that lasts."</p>
    </div>

    <footer class="footer">
      <div class="footer__brand"><i></i>Brightmoor Labs</div>
      <p class="footer__tag">Making learning that sticks through AI-driven sustainment and behavioral science.</p>
      <div class="footer__col footer__col--links"><h4>Quick Links</h4>Home<br>Approach<br>Programs<br>About<br>Contact</div>
      <div class="footer__col footer__col--touch"><h4>Get in Touch</h4>
        <svg class="ico" viewBox="0 0 12 10"><rect x="0.5" y="0.5" width="11" height="9" fill="none" stroke="currentColor"/><path d="M1 1l5 4 5-4" fill="none" stroke="currentColor"/></svg>contact@brightmoorlabs.com<br>
        <svg class="ico" viewBox="0 0 12 10"><path d="M2 1l2 0 1 2-1 1q1 2 3 3l1-1 2 1v2q-6 0-8-8z" fill="none" stroke="currentColor"/></svg>+1 (555) 014-2290<br>
        <svg class="ico" viewBox="0 0 12 10"><path d="M6 9.5C3 6 2.5 5 2.5 4a3.5 3.5 0 017 0c0 1-.5 2-3.5 5.5z" fill="none" stroke="currentColor"/></svg>2750 Harlow Ave Suite 210<br><span style="margin-left:9px">Denver, CO 80205</span>
        <div class="socials"><span></span><span></span></div>
      </div>
      <div class="footer__rule"></div>
      <div class="footer__copy">© 2025 Brightmoor Labs. All rights reserved.</div>
      <div class="footer__legal"><span>Terms</span><span>Privacy</span></div>
    </footer>
  </section>

</div>
</body>
</html>
```